4nowvanta business card
4nowvanta busines card
Professional
Lucinda Harwell Brophy
Principal Partner
42 Juniper Street
Arlington, MA 02319
lucinda@4nowvanta.com
www.4nowvanta.com
I uploaded the full folder, because I was having a little trouble saving the .ai and .eps files

```html
<!DOCTYPE html>
<html lang="en">
<head>
<meta charset="utf-8">
<title>4nowvanta Stationery</title>
<link href="https://fonts.googleapis.com/css2?family=Open+Sans:wght@400;700&display=swap" rel="stylesheet">
<style>
  :root{
    --bg:#3b3b3d;
    --paper:#ffffff;
    --paper-shade:#e9ecee;
    --green:#1f8b2f;
    --blue:#1d3c8c;
    --ink:#333a40;
    --muted:#8a9096;
    --watermark:#eef2ef;
  }
  *{box-sizing:border-box;margin:0;padding:0}
  html,body{width:1200px;height:310px;overflow:hidden}
  body{background:var(--bg);font-family:"Open Sans",Arial,sans-serif;position:relative;color:var(--ink)}
  .item{position:absolute;background:var(--paper);box-shadow:0 2px 5px rgba(0,0,0,.45);overflow:hidden}
  .brand{display:flex;align-items:center;gap:4px}
  .brand-mark{background:var(--green);flex:none}
  .brand-name{font-weight:700;color:var(--green);white-space:nowrap}
  .brand.invert .brand-mark{background:#fff}
  .brand.invert .brand-name{color:#fff}

  /* identity block */
  .identity{position:absolute;left:8px;top:8px;width:150px}
  .identity .brand{flex-direction:column;align-items:flex-start;gap:4px}
  .identity .brand-mark{width:52px;height:52px}
  .identity .brand-name{font-size:13px}
  .identity .tagline{font-size:6px;color:#cfd3d6;margin-top:2px}
  .identity .set-label{font-size:6px;color:#b9bec2;margin-top:8px}

  /* business cards */
  .card-front{left:8px;top:148px;width:124px;height:56px}
  .card-front .brand{position:absolute;left:7px;top:8px;flex-direction:column;align-items:flex-start;gap:2px}
  .card-front .brand-mark{width:14px;height:14px}
  .card-front .brand-name{font-size:6px}
  .card-front .details{position:absolute;left:62px;top:9px;font-size:4px;line-height:6px;color:var(--ink);white-space:nowrap}
  .card-front .details strong{font-size:4.5px;font-weight:700}
  .card-plain{left:8px;top:233px;width:106px;height:50px;display:flex;align-items:center;justify-content:center}
  .card-plain .brand-mark{width:12px;height:12px}
  .card-plain .brand-name{font-size:7px}
  .card-green{left:121px;top:233px;width:104px;height:50px;background:var(--green);display:flex;align-items:center;justify-content:center}
  .card-green .brand-mark{width:12px;height:12px}
  .card-green .brand-name{font-size:7px}

  /* letterheads */
  .letterhead{top:12px;width:190px;height:282px}
  .letterhead.one{left:265px}
  .letterhead.two{left:491px}
  .letterhead .brand{position:absolute;left:14px;top:12px}
  .letterhead .brand-mark{width:14px;height:14px}
  .letterhead .brand-name{font-size:7px}
  .letterhead .contact{position:absolute;left:90px;top:12px;font-size:3.6px;line-height:5px;color:var(--muted)}
  .letterhead .watermark{position:absolute;left:40px;top:70px;width:110px;height:110px;background:var(--watermark)}
  .letterhead .swoosh{position:absolute;left:0;bottom:0;width:100%;height:32px}
  .letterhead .footer-web{position:absolute;left:0;right:0;bottom:3px;text-align:center;font-size:3.5px;color:var(--muted)}

  /* note cards */
  .note{left:700px;width:146px;height:108px}
  .note.top{top:53px}
  .note.bottom{top:173px}
  .note .brand{position:absolute;left:10px;top:8px}
  .note .brand-mark{width:11px;height:11px}
  .note .brand-name{font-size:6px}
  .note .contact{position:absolute;left:10px;top:24px;font-size:3.4px;line-height:4.5px;color:var(--muted)}
  .note .swoosh{position:absolute;left:0;bottom:0;width:100%;height:20px}
  .note .footer-web{position:absolute;left:0;right:0;bottom:2px;text-align:center;font-size:3.2px;color:var(--muted)}

  /* envelopes */
  .envelope{left:864px;width:312px;height:70px}
  .envelope.back-colour{top:48px}
  .envelope.back-white{top:124px}
  .envelope.front{top:208px;height:76px}
  .envelope svg.flap{position:absolute;left:0;top:0;width:100%;height:100%}
  .envelope .brand{position:absolute;left:10px;top:8px}
  .envelope .brand-mark{width:11px;height:11px}
  .envelope .brand-name{font-size:6px}
  .envelope .return{position:absolute;left:10px;top:23px;font-size:3.4px;line-height:4.5px;color:var(--muted)}
  .envelope .stamp{position:absolute;right:10px;top:8px;width:14px;height:16px;border:1px solid var(--paper-shade)}
</style>
</head>
<body>

  <section class="identity">
    <div class="brand">
      <span class="brand-mark"></span>
      <span class="brand-name">4nowvanta</span>
    </div>
    <p class="tagline">Build Your Way, Grow Your Vision</p>
    <p class="set-label">Stationery Concepts</p>
  </section>

  <article class="item card-front">
    <div class="brand"><span class="brand-mark"></span><span class="brand-name">4nowvanta</span></div>
    <div class="details">
      <strong>Lucinda Harwell Brophy</strong><br>
      Principal Partner<br>
      42 Juniper Street<br>
      Arlington, MA 02319<br>
      lucinda@4nowvanta.com<br>
      www.4nowvanta.com
    </div>
  </article>

  <article class="item card-plain">
    <div class="brand"><span class="brand-mark"></span><span class="brand-name">4nowvanta</span></div>
  </article>

  <article class="item card-green">
    <div class="brand invert"><span class="brand-mark"></span><span class="brand-name">4nowvanta</span></div>
  </article>

  <article class="item letterhead one">
    <div class="brand"><span class="brand-mark"></span><span class="brand-name">4nowvanta</span></div>
    <div class="contact">42 Juniper Street<br>Arlington, MA 02319<br>lucinda@4nowvanta.com</div>
    <div class="watermark" role="img" aria-label="Faint brand backdrop"></div>
    <svg class="swoosh" viewBox="0 0 190 32" preserveAspectRatio="none">
      <path d="M0 22 Q95 10 190 18 L190 32 L0 32 Z" fill="var(--green)"/>
      <path d="M0 24 Q95 14 190 21" stroke="var(--blue)" stroke-width="1.5" fill="none"/>
      <path d="M0 26 Q95 20 190 32 L0 32 Z" fill="#fff"/>
    </svg>
    <div class="footer-web">www.4nowvanta.com</div>
  </article>

  <article class="item letterhead two">
    <div class="brand"><span class="brand-mark"></span><span class="brand-name">4nowvanta</span></div>
    <div class="contact">42 Juniper Street<br>Arlington, MA 02319<br>lucinda@4nowvanta.com</div>
    <div class="watermark" role="img" aria-label="Faint brand backdrop"></div>
    <svg class="swoosh" viewBox="0 0 190 32" preserveAspectRatio="none">
      <path d="M0 22 Q95 10 190 18 L190 32 L0 32 Z" fill="var(--green)"/>
      <path d="M0 24 Q95 14 190 21" stroke="var(--blue)" stroke-width="1.5" fill="none"/>
      <path d="M0 26 Q95 20 190 32 L0 32 Z" fill="#fff"/>
    </svg>
    <div class="footer-web">www.4nowvanta.com</div>
  </article>

  <article class="item note top">
    <div class="brand"><span class="brand-mark"></span><span class="brand-name">4nowvanta</span></div>
    <div class="contact">42 Juniper Street<br>Arlington, MA 02319</div>
    <svg class="swoosh" viewBox="0 0 146 20" preserveAspectRatio="none">
      <path d="M0 12 Q73 4 146 10 L146 20 L0 20 Z" fill="var(--green)"/>
      <path d="M0 16 Q73 12 146 20 L0 20 Z" fill="#fff"/>
    </svg>
    <div class="footer-web">www.4nowvanta.com</div>
  </article>

  <article class="item note bottom">
    <div class="brand"><span class="brand-mark"></span><span class="brand-name">4nowvanta</span></div>
    <div class="contact">42 Juniper Street<br>Arlington, MA 02319</div>
    <svg class="swoosh" viewBox="0 0 146 20" preserveAspectRatio="none">
      <path d="M0 12 Q73 4 146 10 L146 20 L0 20 Z" fill="var(--green)"/>
      <path d="M0 16 Q73 12 146 20 L0 20 Z" fill="#fff"/>
    </svg>
    <div class="footer-web">www.4nowvanta.com</div>
  </article>

  <article class="item envelope back-colour">
    <svg class="flap" viewBox="0 0 312 70" preserveAspectRatio="none">
      <defs>
        <linearGradient id="flapFill" x1="0" y1="0" x2="0" y2="1">
          <stop offset="0" stop-color="var(--blue)"/>
          <stop offset="1" stop-color="var(--green)"/>
        </linearGradient>
      </defs>
      <path d="M0 0 L312 0 L312 8 L156 44 L0 8 Z" fill="url(#flapFill)"/>
      <path d="M0 70 L140 38 M312 70 L172 38" stroke="var(--paper-shade)" stroke-width="1"/>
    </svg>
  </article>

  <article class="item envelope back-white">
    <svg class="flap" viewBox="0 0 312 70" preserveAspectRatio="none">
      <path d="M0 0 L156 40 L312 0" stroke="#d5d9dc" stroke-width="1" fill="#f7f8f9"/>
      <path d="M0 70 L140 38 M312 70 L172 38" stroke="var(--paper-shade)" stroke-width="1"/>
    </svg>
  </article>

  <article class="item envelope front">
    <div class="brand"><span class="brand-mark"></span><span class="brand-name">4nowvanta</span></div>
    <div class="return">42 Juniper Street<br>Arlington, MA 02319</div>
    <div class="stamp"></div>
  </article>

</body>
</html>
```